Professional Baby Bottle Bank Print Design

We need a baby bottle design that is 4.25" wide x 2.28" tall with a maximum of 6 colors (white is counted as a color).

The bottle design needs to be fun but professional. Bottles with cartoon images on it will be rejected immediately.

The bottle design wraps around the bottle. See examples here: https://wendrix.net/cat/BabyBottles/OrvelJarsKit/5

Minimum font size is 10pt.

The bottle design must have the following text on it:
Main Text: Cherish Every Life
Paragraph text: Our ministry’s aim is to not only save unborn babies, but to provide love, support, and life-saving resources for vulnerable women in our community. By filling this bottle with cash, checks, and spare coins and returning it on collection day, you are truly saving and changing lives!
Optional text: Thank you!

We are including an example file and a template file. You do NOT have to use the template - but your file has to be the exact size mentioned. If you don't design as well as our sample, please don't waste our time by spamming us with hundreds of designs. We will ban design houses that spam us with designs that are more layouts (and not well designed).

Please note - white is a color. You don't have to do a box - but anything you don't make white will be see-through.

We will take the winners of this contest to a survey with the customers. We may choose two and edit the text of one slightly to be different. We must know the fonts used.

No gradients unless they are half-toned with relatively big sized dots.

Target Market(s)

Church Attendees coming from a Pregnancy Center

Industry/Entity Type

Religious Christian Churches

Requirements
Must have
• Professional, great palette, wording as described.
Nice to have
• Integrated design across the whole space with areas for text (no text all the way across)
Should not have
• Cartoon figures; elements shoved together that don't go together (i.e. - actually design something)

```html
<!DOCTYPE html>
<html lang="en">
<head>
<meta charset="utf-8">
<title>Cherish Every Life – Baby Bottle Label</title>
<link rel="stylesheet" href="https://fonts.googleapis.com/css2?family=Andika:wght@400;700&family=Caveat:wght@600&display=swap">
<style>
  :root {
    --stage: #4d4d4d;
    --paper: #fbeef6;
    --pink: #e887b0;
    --teal: #9ed8d2;
    --mint: #7fe3c4;
    --peach: #fdd3a8;
    --ink: #111111;
  }
  * { margin: 0; padding: 0; box-sizing: border-box; }
  html, body { width: 1200px; height: 876px; overflow: hidden; }
  body { background: var(--stage); position: relative; }

  .label {
    position: absolute;
    left: 40px; top: 137px;
    width: 1120px; height: 601px;
    overflow: hidden;
    background:
      radial-gradient(circle at 0% 0%, var(--peach) 0, rgba(253,211,168,0) 28%),
      radial-gradient(circle at 100% 0%, var(--mint) 0, rgba(127,227,196,0) 22%),
      radial-gradient(circle at 0% 100%, var(--mint) 0, rgba(127,227,196,0) 20%),
      radial-gradient(circle at 100% 100%, var(--peach) 0, rgba(253,211,168,0) 22%),
      radial-gradient(ellipse at 78% 40%, #f4f7c8 0, rgba(244,247,200,0) 30%),
      var(--paper);
  }

  .blob { position: absolute; border-radius: 50%; filter: blur(1px); }
  .blob--blue { left: 690px; top: 32px; width: 46px; height: 24px; background: linear-gradient(90deg, #8fb8f2, #6fd8e8); }
  .blob--orange { left: 290px; top: 81px; width: 54px; height: 28px; background: linear-gradient(90deg, #f8b7a0, #fbd4a4); }
  .blob--green { left: 845px; top: 74px; width: 56px; height: 30px; background: #b6efc2; }
  .blob--violet { left: 367px; top: 570px; width: 46px; height: 24px; background: linear-gradient(90deg, #b78be8, #7ac8ee); }

  .org-name {
    position: absolute;
    left: 92px; top: 40px;
    width: 260px;
    font-family: "Andika", sans-serif;
    font-weight: 700;
    font-size: 62px;
    line-height: 70px;
    color: var(--pink);
  }

  .illustration {
    position: absolute;
    left: 87px; top: 253px;
    width: 262px; height: 325px;
    border-radius: 48% 52% 50% 50% / 40% 40% 60% 60%;
    background: radial-gradient(ellipse at 50% 40%, #ffffff 0, #ffffff 30%, #f2a9c7 62%, var(--pink) 100%);
  }

  .message {
    position: absolute;
    left: 501px; top: 62px;
    width: 563px; height: 500px;
  }
  .message__frame {
    position: absolute;
    inset: 0;
    border: 3px solid var(--pink);
    border-radius: 48px;
  }
  .message__frame--inner {
    inset: 6px;
    border-color: var(--teal);
    border-radius: 42px;
  }
  .message__text {
    position: absolute;
    right: 16px; top: 48px;
    font-family: "Andika", sans-serif;
    font-size: 30px;
    line-height: 42px;
    color: var(--ink);
    text-align: right;
    white-space: nowrap;
  }
  .message__thanks {
    position: absolute;
    right: 64px; top: 440px;
    font-family: "Caveat", cursive;
    font-weight: 600;
    font-size: 44px;
    line-height: 1;
    color: var(--ink);
  }
</style>
</head>
<body>
  <section class="label" aria-label="Cherish Every Life baby bottle label">
    <span class="blob blob--blue"></span>
    <span class="blob blob--orange"></span>
    <span class="blob blob--green"></span>
    <span class="blob blob--violet"></span>

    <h1 class="org-name">Cherish<br>Every<br>Life</h1>

    <div class="illustration" role="img" aria-label="Line illustration of a mother cradling her newborn, in pink and teal"></div>

    <div class="message">
      <span class="message__frame"></span>
      <span class="message__frame message__frame--inner"></span>
      <p class="message__text">Our ministry’s aim is to not only save<br>unborn babies, but to provide love,<br>support, and life-saving resources<br>for vulnerable women in our<br>community.<br>By filling this bottle with cash,<br>checks, and spare coins and<br>returning it on collection day, you<br>are truly saving and changing lives!</p>
      <p class="message__thanks">Thank You!</p>
    </div>
  </section>
</body>
</html>
```